International Parcel Forwarder needs website redesign and logo

We need an updated website design to make our existing site look more modern, global and trustworthy. Current site
www.parvento.com -- we do not want to rebuild headers or at this point do copyright we are simply looking to make the site pop:)
The service we provide is for shoppers living outside the USA looking to shop here and save money on shipping or get access to stores that won't ship internationally or accept international payment.
Target Market(s)
Online shoppers living outside the USA
Industry/Entity Type
Shipping
Logo Text
US shopping, global shipping
Coding
Coded - Design and coding required
Number of Pages Required
5+ page
Font styles to use

```html
<!DOCTYPE html>
<html lang="en">
<head>
<meta charset="utf-8">
<title>Parvento — Shop at any U.S. retailer, ship anywhere</title>
<link rel="stylesheet" href="https://fonts.googleapis.com/css2?family=Lato:wght@400;700&family=Montserrat:wght@500;600&family=Roboto:wght@400;500&display=swap">
<style>
  :root {
    --purple: #3b2d86;
    --purple-dark: #2b2347;
    --purple-deep: #241c40;
    --orange: #f5a030;
    --orange-dark: #e08a1c;
    --charcoal: #3a3a3a;
    --ink: #333333;
    --muted: #666666;
    --light: #f1f1f1;
    --white: #ffffff;
  }
  * { margin: 0; padding: 0; box-sizing: border-box; }
  html, body { width: 1200px; height: 3066px; overflow: hidden; }
  body { position: relative; background: var(--white); font-family: "Roboto", Arial, sans-serif; color: var(--ink); }
  .abs { position: absolute; }

  /* Header */
  .topbar { left: 0; top: 0; width: 1200px; height: 135px; background: var(--charcoal); }
  .brand { left: 106px; top: 20px; font-family: "Montserrat", sans-serif; font-weight: 600; font-size: 30px; color: var(--orange); letter-spacing: 1px; }
  .btn-top { top: 25px; height: 38px; background: var(--orange); color: var(--ink); font-family: "Lato", sans-serif; font-size: 15px; font-weight: 700; display: flex; align-items: center; justify-content: center; gap: 10px; letter-spacing: .5px; }
  .btn-login { left: 854px; width: 111px; }
  .btn-signup { left: 977px; width: 121px; }
  .mainnav { left: 147px; top: 86px; width: 667px; height: 49px; background: var(--purple); }
  .mainnav a { position: absolute; top: 0; color: var(--white); text-decoration: none; font-family: "Lato", sans-serif; font-size: 14px; font-weight: 700; line-height: 49px; white-space: nowrap; }
  .nav-search { left: 814px; top: 86px; width: 50px; height: 49px; background: var(--purple-deep); display: flex; align-items: center; justify-content: center; }
  .nav-social { left: 864px; top: 86px; width: 195px; height: 49px; background: var(--purple-dark); display: flex; align-items: center; justify-content: space-around; padding: 0 14px; }
  .nav-social span { width: 10px; height: 10px; border-radius: 50%; background: #5d4f9c; }

  /* Hero */
  .hero { left: 0; top: 135px; width: 1200px; height: 550px; background: linear-gradient(90deg, #ececec 0%, #e2e2e2 45%, #d0cfcd 100%); }
  .hero-photo { left: 531px; top: 135px; width: 669px; height: 550px; background: radial-gradient(ellipse at 55% 45%, #b66f7a 0%, #8d6b5c 35%, #a8a29a 70%, #d4d1cc 100%); }
  .hero-kicker { left: 108px; top: 288px; font-family: "Lato", sans-serif; font-size: 24px; color: var(--ink); }
  .hero-title { left: 108px; top: 326px; font-family: "Lato", sans-serif; font-size: 32px; font-weight: 700; color: var(--ink); }
  .hero-copy { left: 108px; top: 382px; width: 420px; font-size: 14px; line-height: 22px; color: #555; }
  .hero-btn { left: 108px; top: 493px; width: 192px; height: 49px; background: var(--orange); color: var(--ink); font-family: "Lato", sans-serif; font-size: 16px; font-weight: 700; display: flex; align-items: center; justify-content: center; }
  .slide-arrow { top: 387px; width: 42px; height: 44px; background: #555; display: flex; align-items: center; justify-content: center; }
  .slide-prev { left: 0; }
  .slide-next { left: 1158px; }

  /* Service cards */
  .service { top: 630px; width: 180px; height: 304px; }
  .service-head { height: 214px; background: var(--purple); display: flex; flex-direction: column; align-items: center; padding-top: 38px; }
  .service-head h3 { margin-top: 34px; font-family: "Lato", sans-serif; font-size: 14px; font-weight: 700; color: var(--orange); }
  .service-body { height: 90px; background: var(--orange); color: var(--purple-dark); font-size: 11px; line-height: 15px; text-align: center; padding: 14px 12px; }

  /* Packing */
  .section-num { font-family: "Montserrat", sans-serif; font-size: 40px; font-weight: 600; color: #ececec; }
  .section-title { font-family: "Montserrat", sans-serif; font-size: 28px; font-weight: 500; color: var(--purple); letter-spacing: 1px; }
  .packing-copy { left: 96px; top: 806px; width: 420px; font-size: 13px; line-height: 19px; color: #555; }
  .packing-list { left: 96px; top: 866px; list-style: none; font-size: 12.5px; line-height: 24.5px; color: #555; }
  .packing-list li::before { content: "•"; color: var(--orange); margin-right: 9px; }

  /* Calculator */
  .form-label { font-size: 13px; color: var(--ink); }
  .field { border: 1px solid #d6d6d6; background: var(--white); font-size: 12px; color: #aaa; display: flex; align-items: center; padding-left: 12px; }
  .option { font-size: 12px; color: #555; display: flex; align-items: center; gap: 8px; }
  .dot { width: 12px; height: 12px; border-radius: 50%; border: 1px solid #bbb; display: inline-block; position: relative; }
  .dot.on::after { content: ""; position: absolute; left: 2px; top: 2px; width: 6px; height: 6px; border-radius: 50%; background: var(--purple); }
  .box { width: 12px; height: 12px; border: 1px solid #bbb; display: inline-block; position: relative; }
  .box.on::after { content: ""; position: absolute; left: 2px; top: 2px; width: 6px; height: 6px; border-radius: 50%; background: var(--purple); }
  .calc-btn { left: 429px; top: 1347px; width: 147px; height: 41px; background: var(--orange); border: 1px solid var(--orange-dark); font-family: "Lato", sans-serif; font-size: 14px; font-weight: 700; color: var(--ink); display: flex; align-items: center; justify-content: center; }
  .courier-photo { left: 783px; top: 1051px; width: 321px; height: 425px; background: radial-gradient(ellipse at 50% 55%, #2d67b8 0%, #3f78c6 38%, #c7a57f 60%, #ffffff 78%); }

  /* Why */
  .why { left: 0; top: 1498px; width: 1200px; height: 438px; background: linear-gradient(90deg, #2f2f2f, #4a4a4a 50%, #333); }
  .why h2 { position: absolute; left: 0; top: 60px; width: 1200px; text-align: center; font-family: "Montserrat", sans-serif; font-weight: 500; font-size: 30px; color: var(--white); letter-spacing: 1px; }
  .why-col { top: 1630px; width: 240px; text-align: center; color: var(--white); }
  .why-col .icon { height: 90px; display: flex; align-items: center; justify-content: center; }
  .why-col h3 { margin-top: 38px; font-family: "Montserrat", sans-serif; font-weight: 500; font-size: 20px; letter-spacing: 1px; }
  .why-col p { font-size: 13px; line-height: 17px; margin-top: 10px; }

  /* Video */
  .how-title { left: 0; top: 1995px; width: 1200px; text-align: center; font-family: "Montserrat", sans-serif; font-weight: 500; font-size: 30px; color: var(--ink); letter-spacing: 1px; }
  .video { left: 114px; top: 2083px; width: 978px; height: 400px; background: #000; }
  .video-art { left: 247px; top: 2083px; width: 712px; height: 400px; background: linear-gradient(135deg, #2ea3e6 0%, #6cc7f0 50%, #27a0e3 100%); }
  .video-brand { left: 144px; top: 2157px; font-family: "Montserrat", sans-serif; font-weight: 600; font-size: 15px; color: var(--orange); }
  .video-tools { left: 1054px; top: 2092px; display: flex; flex-direction: column; gap: 7px; }
  .video-tools span { width: 24px; height: 24px; background: #222; border-radius: 2px; display: block; }
  .video-bar { left: 124px; top: 2440px; width: 958px; height: 34px; display: flex; align-items: center; gap: 12px; }
  .play { width: 44px; height: 32px; background: #1a1a1a; display: flex; align-items: center; justify-content: center; }
  .track { flex: 1; height: 8px; background: #3a3a3a; }
  .video-badge { font-family: "Lato", sans-serif; font-size: 12px; font-weight: 700; color: var(--white); padding-right: 10px; }

  /* Clients */
  .clients { left: 0; top: 2567px; width: 1200px; height: 123px; background: var(--orange); }
  .clients-label { left: 0; top: 2567px; width: 400px; height: 123px; background: #eeeeee; clip-path: polygon(0 0, 295px 0, 370px 123px, 0 123px); }
  .clients-label span { position: absolute; left: 70px; top: 44px; font-family: "Montserrat", sans-serif; font-weight: 500; font-size: 30px; color: var(--ink); }
  .client-logo { top: 2609px; width: 140px; height: 40px; line-height: 40px; text-align: center; white-space: nowrap; font-family: "Montserrat", sans-serif; font-weight: 600; font-size: 26px; color: var(--ink); }
  .client-arrow { top: 2615px; }

  /* Footer */
  .footer { left: 0; top: 2690px; width: 1200px; height: 376px; background: var(--purple-dark); }
  .footer-links { left: 0; top: 2772px; width: 1200px; display: flex; justify-content: center; font-family: "Lato", sans-serif; font-size: 16px; color: var(--white); letter-spacing: .5px; }
  .footer-links span { padding: 0 12px; }
  .footer-rule { height: 1px; background: #4c4470; }
  .partner-title { left: 0; top: 2855px; width: 1200px; text-align: center; font-family: "Montserrat", sans-serif; font-weight: 500; font-size: 22px; color: var(--white); letter-spacing: 1px; }
  .partner { top: 2922px; width: 140px; text-align: center; white-space: nowrap; font-family: "Montserrat", sans-serif; font-weight: 600; font-size: 20px; color: #d8d8d8; }
  .legal { top: 3018px; font-family: "Lato", sans-serif; font-size: 15px; color: var(--white); letter-spacing: .4px; }
</style>
</head>
<body>

<header>
  <div class="abs topbar"></div>
  <div class="abs brand">PARVENTO</div>
  <div class="abs btn-top btn-login">LOG IN
    <svg width="16" height="16" viewBox="0 0 16 16"><circle cx="8" cy="8" r="7" fill="none" stroke="#333" stroke-width="1.5"/><path d="M6 4.5 L10.5 8 L6 11.5Z" fill="#333"/></svg>
  </div>
  <div class="abs btn-top btn-signup">SIGN UP
    <svg width="14" height="16" viewBox="0 0 14 16"><circle cx="7" cy="4" r="3.5" fill="#333"/><path d="M1 15 Q7 6 13 15Z" fill="#333"/></svg>
  </div>
  <nav class="abs mainnav">
    <a href="#" style="left:18px">HOW IT WORKS</a>
    <a href="#" style="left:175px">PARVENTO PRICING</a>
    <a href="#" style="left:337px">LEARN MORE</a>
    <a href="#" style="left:473px">BLOG</a>
    <a href="#" style="left:550px">CONTACT US</a>
  </nav>
  <div class="abs nav-search">
    <svg width="18" height="18" viewBox="0 0 18 18"><circle cx="7.5" cy="7.5" r="5.5" fill="none" stroke="#fff" stroke-width="2.2"/><path d="M11.5 11.5 L16 16" stroke="#fff" stroke-width="2.4"/></svg>
  </div>
  <div class="abs nav-social"><span></span><span></span><span></span><span></span></div>
</header>

<section class="hero-section">
  <div class="abs hero" role="img" aria-label="Faint world map on a light grey background"></div>
  <div class="abs hero-photo" role="img" aria-label="Photograph of a worker in a hi-vis vest beside a netted pallet of colourful parcels in a cargo hold"></div>
  <div class="abs hero-kicker">Shop At Any U.S.</div>
  <div class="abs hero-title">Retailer. Ship Anywhere.</div>
  <p class="abs hero-copy">Lorem ipsum dolor sit amet, consectetur adipiscing elit, sed do eiusmod tempor incididunt ut labore et dolore magna aliqua. Ut enim ad minim veniam, quis nostrud exercitation ex ea commodo consequat..</p>
  <div class="abs hero-btn">Learn More</div>
  <div class="abs slide-arrow slide-prev"><svg width="12" height="14" viewBox="0 0 12 14"><path d="M9 1 L3 7 L9 13" fill="none" stroke="#fff" stroke-width="2.5"/></svg></div>
  <div class="abs slide-arrow slide-next"><svg width="12" height="14" viewBox="0 0 12 14"><path d="M3 1 L9 7 L3 13" fill="none" stroke="#fff" stroke-width="2.5"/></svg></div>

  <div class="abs service" style="left:546px">
    <div class="service-head">
      <svg width="70" height="70" viewBox="0 0 70 70" fill="none" stroke="#fff" stroke-width="2.5"><path d="M8 42 H62 L54 56 H16Z"/><rect x="20" y="26" width="30" height="16"/><rect x="28" y="14" width="12" height="12"/><path d="M6 62 Q14 58 22 62 T38 62 T54 62 T66 62"/></svg>
      <h3>SEA SHIPPING</h3>
    </div>
    <div class="service-body">We want to ensure that it's as easy as possible to use the site to get.</div>
  </div>
  <div class="abs service" style="left:740px">
    <div class="service-head">
      <svg width="70" height="70" viewBox="0 0 70 70" fill="none" stroke="#fff" stroke-width="2.5"><path d="M4 34 H66"/><ellipse cx="35" cy="36" rx="14" ry="10"/><path d="M35 26 V14 M35 46 V56 M28 56 H42"/><circle cx="30" cy="36" r="2"/><circle cx="40" cy="36" r="2"/></svg>
      <h3>AIR SHIPPING</h3>
    </div>
    <div class="service-body">Shipments moving, whether you've worked with us for years completely new.</div>
  </div>
  <div class="abs service" style="left:934px">
    <div class="service-head">
      <svg width="70" height="70" viewBox="0 0 70 70" fill="none" stroke="#fff" stroke-width="2.5"><rect x="18" y="8" width="34" height="44" rx="6"/><rect x="24" y="16" width="22" height="14"/><circle cx="26" cy="42" r="3"/><circle cx="44" cy="42" r="3"/><path d="M22 52 L14 64 M48 52 L56 64 M18 60 H52"/></svg>
      <h3>LAND SHIPPING</h3>
    </div>
    <div class="service-body">International shipping. For further assistance, please get in touch.</div>
  </div>
</section>

<section class="packing">
  <div class="abs section-num" style="left:90px;top:706px">01</div>
  <h2 class="abs section-title" style="left:96px;top:726px">PACKING &amp; STORAGE</h2>
  <p class="abs packing-copy">Bringing you industry-specific expertise; whatever you're shipping, wherever you're shipping it.</p>
  <ul class="abs packing-list">
    <li>Shipper delivers a professional, efficient service</li>
    <li>Tailored to the specific needs of your business.</li>
    <li>Our services are designed around you.</li>
  </ul>
</section>

<section class="calculator">
  <div class="abs section-num" style="left:90px;top:1040px">02</div>
  <h2 class="abs section-title" style="left:100px;top:1059px">CALCULATE SHIPPING</h2>

  <div class="abs form-label" style="left:100px;top:1150px">Distance</div>
  <div class="abs option" style="left:100px;top:1176px"><span class="dot on"></span>Domestic</div>
  <div class="abs option" style="left:214px;top:1176px"><span class="dot"></span>International</div>
  <div class="abs form-label" style="left:100px;top:1210px">Weight</div>
  <div class="abs field" style="left:100px;top:1237px;width:186px;height:34px"></div>
  <div class="abs form-label" style="left:100px;top:1288px">Cargo Size</div>
  <div class="abs field" style="left:100px;top:1312px;width:66px;height:37px">cm</div>
  <div class="abs option" style="left:176px;top:1322px">x</div>
  <div class="abs field" style="left:194px;top:1312px;width:66px;height:37px">cm</div>
  <div class="abs form-label" style="left:100px;top:1365px">Fragile</div>
  <div class="abs field" style="left:100px;top:1390px;width:209px;height:35px;color:#333;justify-content:space-between;padding-right:12px">YES<svg width="8" height="5" viewBox="0 0 8 5"><path d="M0 0 H8 L4 5Z" fill="#333"/></svg></div>

  <div class="abs form-label" style="left:429px;top:1150px">Extra Services</div>
  <div class="abs option" style="left:429px;top:1178px"><span class="box on"></span>Quick Delivery</div>
  <div class="abs option" style="left:429px;top:1202px"><span class="box"></span>Warranty</div>
  <div class="abs option" style="left:429px;top:1227px"><span class="box"></span>Gift Box</div>
  <div class="abs option" style="left:429px;top:1263px;font-size:11.5px">The Field below will show the double of the number about $</div>
  <div class="abs field" style="left:429px;top:1294px;width:188px;height:39px;background:#e9e9e9;color:#555">$200</div>
  <div class="abs calc-btn">CALCULATE</div>

  <div class="abs courier-photo" role="img" aria-label="Photograph of a smiling courier in a blue polo shirt holding a clipboard and a cardboard parcel"></div>
</section>

<section>
  <div class="abs why" role="img" aria-label="Darkened photograph of an office team at work">
    <h2>WHY USE PARVENTO</h2>
  </div>
  <div class="abs why-col" style="left:66px">
    <div class="icon"><svg width="80" height="84" viewBox="0 0 80 84" fill="#fff"><path d="M36 20 C54 20 64 32 62 48 L68 58 L62 60 V72 H50 V84 H22 V66 C12 58 10 46 14 36 C18 26 26 20 36 20Z"/><circle cx="40" cy="42" r="8" fill="#3a3a3a"/><g stroke="#fff" stroke-width="3"><path d="M40 4 V14 M22 10 L28 18 M58 10 L52 18 M12 24 L20 28 M68 24 L60 28"/></g></svg></div>
    <h3>EXPERIENCE</h3>
    <p>30 years experience in<br>international shipping.</p>
    <p>Excellent customer service</p>
  </div>
  <div class="abs why-col" style="left:342px">
    <div class="icon" style="font-family:'Montserrat',sans-serif;font-size:86px;font-weight:600;line-height:1">$</div>
    <h3>VALUE</h3>
    <p>Discounted shipping rates<br>with major carriers</p>
    <p>No membership or joining fees</p>
    <p>Low consolidation fees</p>
  </div>
  <div class="abs why-col" style="left:618px">
    <div class="icon"><svg width="80" height="72" viewBox="0 0 80 72"><path d="M40 66 L8 34 C-2 22 6 4 22 4 C30 4 36 9 40 15 C44 9 50 4 58 4 C74 4 82 22 72 34Z" fill="none" stroke="#fff" stroke-width="4"/></svg></div>
    <h3>TRUST</h3>
    <p>Excellent customer service</p>
    <p>A+ rating from the Fair Trade<br>Council</p>
  </div>
  <div class="abs why-col" style="left:892px">
    <div class="icon"><svg width="64" height="80" viewBox="0 0 64 80"><path d="M22 4 H42 L36 18 H28Z M28 20 H36 C54 30 62 50 60 64 C58 76 48 78 32 78 C16 78 6 76 4 64 C2 50 10 30 28 20Z" fill="#fff"/><text x="32" y="62" text-anchor="middle" font-family="Montserrat, sans-serif" font-weight="600" font-size="28" fill="#3a3a3a">$</text></svg></div>
    <h3>SAVINGS</h3>
    <p>No fees to receive packages</p>
    <p>No U.S. sales tax when using our<br>New Hampshire warehouse</p>
    <p>45 days free storage</p>
  </div>
</section>

<section>
  <h2 class="abs how-title">HOW PARVENTO WORKS</h2>
  <div class="abs video"></div>
  <div class="abs video-art" role="img" aria-label="Animated explainer video still: four cartoon shoppers each thinking of goods from different U.S. stores"></div>
  <div class="abs video-brand">PARVENTO</div>
  <div class="abs video-tools"><span></span><span></span><span></span></div>
  <div class="abs video-bar">
    <div class="play"><svg width="12" height="14" viewBox="0 0 12 14"><path d="M0 0 L12 7 L0 14Z" fill="#fff"/></svg></div>
    <div class="track"></div>
    <div class="video-badge">HD Reelio</div>
  </div>
</section>

<section>
  <div class="abs clients"></div>
  <div class="abs clients-label"><span>OUR CLIENTS</span></div>
  <svg class="abs client-arrow" style="left:364px" width="22" height="28" viewBox="0 0 22 28"><path d="M20 0 V28 L0 14Z" fill="#222"/></svg>
  <div class="abs client-logo" style="left:445px">Tinyloom</div>
  <div class="abs client-logo" style="left:641px">Voltmart</div>
  <div class="abs client-logo" style="left:793px">Rivendo</div>
  <div class="abs client-logo" style="left:965px">Bidhaus</div>
  <svg class="abs client-arrow" style="left:1114px" width="22" height="28" viewBox="0 0 22 28"><path d="M0 0 V28 L22 14Z" fill="#222"/></svg>
</section>

<footer>
  <div class="abs footer"></div>
  <div class="abs footer-links"><span>HOW IT WORKS</span>|<span>PRICING</span>|<span>TERMS OF SERVICE</span>|<span>PRIVACY POLICY</span>|<span>CONTACT US</span></div>
  <div class="abs footer-rule" style="left:231px;top:2835px;width:756px"></div>
  <div class="abs partner-title">PARTNERSHIP WITH</div>
  <div class="abs partner" style="left:339px">Swiftpost</div>
  <div class="abs partner" style="left:537px">Nation Mail</div>
  <div class="abs partner" style="left:706px">Kargolink</div>
  <div class="abs footer-rule" style="left:88px;top:2994px;width:1026px"></div>
  <div class="abs legal" style="left:88px">Copyright © 2017 , Parvento. All Rights Reserved.</div>
  <div class="abs legal" style="left:900px;width:214px;text-align:right">Designed by Markforge Team.</div>
</footer>

</body>
</html>
```